IT supplier clean wordpress website - payment guaranteed

Clean website design for a wordpress based website
Design only - PSD delivery with images

current website: www.quorvel.net
please use your imagination and try something out of the box...
We like https://tavrinex.com.au as look and feel, but you don't have to copy it, you can be creative

We like the navigation header and the phone number, but do not need 'instant quote' so the 1300 phone number and the 'lock' icon for login can be on the same line

Site Map:
IT support
VoIP
Internet and Data
Cloud hosting
About
Contact

Our logo is attached, it can be used light or dark.
Our only color used is the warm grey Pantone 8003C hex #877A69

You will only need to design the homepage to win the competition, but the winning designer will be required to supply without extra charges:
1. Home page design
2. A second, standard page template design
3. An icon set in colors appropriate to the site that have icons to match the subjects in these pages:
https://tavrinex.com.au/products/
https://tavrinex.com.au/making-the-switch/
https://tavrinex.com.au/why-tavrinex/
We will create a single page version of the options on https://tavrinex.com.au/solutions/
4.Any images used

Please avoid stock photos that are too common - e.g. smiling woman with headset, try to make the design stand out with simple images and well-designed layout.

Target Market(s)

Mid-size business clients

Industry/Entity Type

It Company

Number of Pages Required

1 page

Requirements
Must have
• Quor logo
• Use Quor color

```html
<!DOCTYPE html>
<html lang="en">
<head>
<meta charset="utf-8">
<title>Quor — IT Support, VoIP, Internet and Cloud</title>
<link rel="stylesheet" href="https://fonts.googleapis.com/css2?family=Raleway:wght@300;400&family=Roboto:wght@300;400&display=swap">
<style>
  :root {
    --warm-grey: #877a69;
    --warm-grey-dark: #6f6354;
    --accent: #e8821f;
    --text: #5f5a55;
    --soft-bg: #f2f0ee;
    --white: #ffffff;
  }
  * { box-sizing: border-box; margin: 0; padding: 0; }
  html, body { width: 1200px; height: 1200px; overflow: hidden; background: var(--white); }
  body { position: relative; font-family: "Raleway", sans-serif; color: var(--text); }

  .site-header { position: absolute; left: 0; top: 0; width: 1200px; height: 126px; }
  .brand { position: absolute; left: 62px; top: 44px; display: flex; align-items: center; gap: 10px;
    font-family: "Raleway", sans-serif; font-weight: 400; font-size: 34px; color: var(--warm-grey); }
  .brand-mark { width: 16px; height: 16px; border: 2px solid var(--warm-grey); border-radius: 3px; }
  .header-contact { position: absolute; right: 54px; top: 40px; display: flex; align-items: center; gap: 18px;
    font-family: "Roboto", sans-serif; font-size: 14.5px; color: var(--warm-grey); font-weight: 400; }
  .main-nav { position: absolute; top: 63px; left: 490px; height: 48px; display: flex; align-items: center;
    font-family: "Roboto", sans-serif; font-weight: 300; font-size: 15px; color: var(--warm-grey); }
  .main-nav a { color: inherit; text-decoration: none; position: absolute; white-space: nowrap; top: 14px; }
  .main-nav .is-current { left: 0; top: 0; width: 48px; height: 48px; border: 1.5px solid var(--warm-grey);
    border-radius: 8px; display: flex; align-items: center; justify-content: center; padding-top: 2px; }
  .accent-rule { position: absolute; left: 0; top: 126px; width: 1200px; height: 3px; background: var(--accent); }

  .hero { position: absolute; left: 0; top: 129px; width: 1200px; height: 448px;
    background: linear-gradient(100deg, #a89a89 0%, #948676 35%, #857868 60%, #9a8d7e 100%); }
  .hero-title { position: absolute; left: 71px; top: 150px; width: 640px; font-family: "Roboto", sans-serif;
    font-weight: 400; font-size: 29px; line-height: 35px; color: var(--white); }
  .hero-button { position: absolute; left: 76px; top: 270px; width: 171px; height: 40px; border: 1.5px solid var(--white);
    border-radius: 6px; color: var(--white); font-family: "Raleway", sans-serif; font-weight: 300; font-size: 23px;
    display: flex; align-items: center; justify-content: center; text-decoration: none; }

  .section-title { position: absolute; left: 0; width: 1200px; text-align: center; font-family: "Raleway", sans-serif;
    font-weight: 400; font-size: 30px; color: var(--warm-grey); }
  .title-divider { position: absolute; height: 14px; }

  .intro-copy { position: absolute; left: 107px; top: 702px; width: 990px; font-size: 15px; line-height: 19.5px; color: var(--text); }
  .intro-copy p + p { margin-top: 19px; }

  .services { position: absolute; left: 0; top: 854px; width: 1200px; height: 346px; background: var(--soft-bg); }
  .service-icon { position: absolute; width: 97px; height: 100px; border-radius: 6px; background: var(--warm-grey);
    display: flex; align-items: center; justify-content: center; }
  .service-name { position: absolute; font-size: 16px; color: var(--accent); font-weight: 400; }
  .service-text { position: absolute; width: 190px; font-size: 12px; line-height: 13.6px; font-weight: 300; color: var(--warm-grey-dark); }
</style>
</head>
<body>

<header class="site-header">
  <div class="brand"><span>Quor</span><span class="brand-mark"></span></div>
  <div class="header-contact">
    <span>+61 (2) 5550 1234</span>
    <svg width="18" height="22" viewBox="0 0 18 22" aria-label="Login">
      <path d="M4 9 V6 a5 5 0 0 1 10 0" fill="none" stroke="var(--accent)" stroke-width="2.6"/>
      <rect x="0" y="9" width="18" height="13" rx="2.5" fill="var(--accent)"/>
      <rect x="8" y="13" width="2.4" height="5" rx="1" fill="var(--white)"/>
    </svg>
  </div>
  <nav class="main-nav">
    <a class="is-current" href="#">Home</a>
    <a href="#" style="left:80px">IT Support</a>
    <a href="#" style="left:188px">VoIP</a>
    <a href="#" style="left:257px">Internet and Data</a>
    <a href="#" style="left:409px">Cloud hosting</a>
    <a href="#" style="left:545px">About</a>
    <a href="#" style="left:620px">Contact</a>
  </nav>
</header>
<div class="accent-rule"></div>

<section class="hero" role="img" aria-label="Photo of a laptop on a desk with notebook, pens and coffee cup, a hand touching the screen">
  <h1 class="hero-title">We Provide IT needs with experience in extensive technologies and platforms with a focus on customer service.</h1>
  <a class="hero-button" href="#">Explore More</a>
</section>

<h2 class="section-title" style="top:617px">do IT better</h2>
<svg class="title-divider" style="left:496px;top:655px" width="164" height="14" viewBox="0 0 164 14">
  <line x1="0" y1="7" x2="164" y2="7" stroke="var(--warm-grey)" stroke-width="1"/>
  <rect x="72" y="0.75" width="13" height="12.5" fill="var(--white)" stroke="var(--accent)" stroke-width="1.5"/>
</svg>

<div class="intro-copy">
  <p>Not only does Quor have highly qualified people, with certifications from Veltrosoft, Norvanet, National Telecom Board amongst others, but importantly we can speak plain English and translate IT questions into a language you can understand and make decisions easier for you.</p>
  <p>We pride ourselves in our skill, integrity and ability to think and act in your best interests - that's what gets us customer referrals time after time. We support the open exchange of ideas in the IT community and put a lot in ourselves.</p>
</div>

<section class="services">
  <h2 class="section-title" style="top:14px;left:5px">Our Services</h2>
  <svg class="title-divider" style="left:501px;top:52px" width="164" height="14" viewBox="0 0 164 14">
    <line x1="0" y1="7" x2="164" y2="7" stroke="var(--warm-grey)" stroke-width="1"/>
    <rect x="73" y="0.75" width="13" height="12.5" fill="var(--soft-bg)" stroke="var(--accent)" stroke-width="1.5"/>
  </svg>

  <div class="service-icon" style="left:174px;top:93px">
    <svg width="60" height="72" viewBox="0 0 60 72" fill="none" stroke="#fff" stroke-width="4">
      <path d="M12 26 a18 18 0 0 1 36 0"/>
      <rect x="8" y="22" width="8" height="14" rx="3" fill="#fff"/>
      <rect x="44" y="22" width="8" height="14" rx="3" fill="#fff"/>
      <circle cx="30" cy="28" r="13"/>
      <path d="M48 36 q0 10 -12 10"/>
      <path d="M5 68 v-6 a14 14 0 0 1 14 -14 h22 a14 14 0 0 1 14 14 v6 z"/>
    </svg>
  </div>
  <div class="service-name" style="left:304px;top:99px">IT Support</div>
  <div class="service-text" style="left:304px;top:124px">We speak many languages including plain English, and will make your experience a pleasure from start to finish.</div>

  <div class="service-icon" style="left:660px;top:97px">
    <svg width="82" height="66" viewBox="0 0 82 66">
      <path d="M18 58 a16 16 0 0 1 -2 -32 a22 22 0 0 1 42 -6 a18 18 0 0 1 8 36 z" fill="#fff"/>
      <rect x="22" y="28" width="34" height="32" rx="3" fill="var(--warm-grey)"/>
      <rect x="25" y="31" width="16" height="26" rx="2" fill="#fff"/>
      <rect x="45" y="28" width="12" height="32" rx="4" fill="#fff" stroke="var(--warm-grey)" stroke-width="2"/>
      <g fill="var(--warm-grey)"><rect x="28" y="34" width="10" height="4"/>
        <rect x="28" y="41" width="2.5" height="2.5"/><rect x="32" y="41" width="2.5" height="2.5"/><rect x="36" y="41" width="2.5" height="2.5"/>
        <rect x="28" y="46" width="2.5" height="2.5"/><rect x="32" y="46" width="2.5" height="2.5"/><rect x="36" y="46" width="2.5" height="2.5"/>
        <rect x="28" y="51" width="2.5" height="2.5"/><rect x="32" y="51" width="2.5" height="2.5"/><rect x="36" y="51" width="2.5" height="2.5"/></g>
    </svg>
  </div>
  <div class="service-name" style="left:784px;top:99px">VoIP</div>
  <div class="service-text" style="left:787px;top:124px">We supplies a wide range of business data connections which are reliable, scalable, fast and represent excellent value for money.</div>

  <div class="service-icon" style="left:173px;top:246px">
    <svg width="64" height="66" viewBox="0 0 64 66">
      <g fill="#fff">
        <ellipse cx="26" cy="10" rx="24" ry="8"/>
        <path d="M2 16 q24 12 48 0 v8 q-24 12 -48 0 z"/>
        <path d="M2 30 q24 12 48 0 v8 q-24 12 -48 0 z"/>
        <path d="M2 44 q24 12 48 0 v8 q-24 12 -48 0 z"/>
        <path d="M48 32 l15 5 v12 q0 12 -15 17 q-15 -5 -15 -17 v-12 z" stroke="var(--warm-grey)" stroke-width="3"/>
      </g>
      <path d="M48 37 v25 q-10 -4 -10 -13 v-8 z" fill="var(--warm-grey)" opacity="0.35"/>
    </svg>
  </div>
  <div class="service-name" style="left:295px;top:242px">Internet and Data</div>
  <div class="service-text" style="left:295px;top:272px">We are specialists in Veltrosoft, fully conversant with Orvix and Lunex. We write websites and applications.</div>

  <div class="service-icon" style="left:659px;top:246px">
    <svg width="82" height="64" viewBox="0 0 82 64" fill="none" stroke="#fff" stroke-width="2.5">
      <path d="M26 52 h-8 a15 15 0 0 1 -2 -30 a22 22 0 0 1 42 -6 a17 17 0 0 1 6 36 h-6"/>
      <rect x="30" y="18" width="22" height="44" rx="4"/>
      <line x1="36" y1="32" x2="46" y2="32"/><line x1="36" y1="38" x2="46" y2="38"/>
      <line x1="36" y1="44" x2="46" y2="44"/><line x1="36" y1="50" x2="46" y2="50"/>
    </svg>
  </div>
  <div class="service-name" style="left:779px;top:249px">Cloud Hosting</div>
  <div class="service-text" style="left:779px;top:279px">Quor provides a range of cloud services, including Software as a service, Infrastructure as a service and Platform as a service.</div>
</section>

</body>
</html>
```